Therapy Services & Training

I provide counseling/therapy to individuals and families. I also travel the country and provide training at conferences.
I would like to see a card which takes my company name and design a logo using the letters "HWAE".
Target Market(s)
Therapists, non-profit organizations, clients looking for therapy
Industry/Entity Type
Training
Contact Information for Business Card
Harborview Wellness Advising & Education LLC
Delia Marsh, M.S.W., LCSW
Clinical Therapist & Trainer
Providing clinical therapy services to individuals, families, couples & children. We also provide life coaching and crisis training.
counselordelia@mailbrook.net
www.harborviewwellnessadvising.com
(555) 214-3092
Cedarvale, IL 60999
(BACK SIDE OF CARD)
We are certified by the Ongoing Professional Lawyer Studies (OPLS) Council of the Prairie High Tribunal to provide Continuing Legal Education (CLE) credits to Illinois attorneys. Call about what courses we offer! (555) 214-3092

```html
<!DOCTYPE html>
<html lang="en">
<head>
<meta charset="utf-8">
<title>Harborview Wellness Advising &amp; Education LLC – Business Card</title>
<link href="https://fonts.googleapis.com/css2?family=Mulish:wght@300;400;500;600;700&display=swap" rel="stylesheet">
<style>
  :root {
    --backdrop: #e4ded2;
    --card: #ffffff;
    --ink: #161616;
    --purple: #5b2a8f;
    --blue: #2f7ec2;
    --soft-blue: #52709e;
    --line-blue: #5a7fae;
  }
  * { margin: 0; padding: 0; box-sizing: border-box; }
  html, body {
    width: 1200px; height: 1000px; overflow: hidden;
    background: var(--backdrop);
    font-family: "Mulish", "Helvetica Neue", Arial, sans-serif;
  }
  .card {
    position: absolute;
    width: 786px; height: 459px;
    background: var(--card);
  }
  .card--back { left: 47px; top: 40px; }
  .card--front { left: 372px; top: 474px; }

  .back-statement {
    position: absolute; left: 39px; top: 122px;
    font-size: 17px; font-weight: 300; line-height: 30px;
    color: var(--soft-blue);
  }
  .back-call {
    position: absolute; left: 39px; top: 303px;
    font-size: 17px; font-weight: 300; color: var(--soft-blue);
  }

  .brand-mark {
    position: absolute; display: flex; align-items: center;
    color: var(--purple); font-weight: 600;
  }
  .brand-mark__dot { border-radius: 50%; background: var(--blue); flex: none; }
  .card--back .brand-mark { left: 540px; top: 222px; font-size: 40px; gap: 14px; }
  .card--back .brand-mark__dot { width: 56px; height: 56px; }
  .card--front .brand-mark { left: 575px; top: 120px; font-size: 30px; gap: 10px; }
  .card--front .brand-mark__dot { width: 40px; height: 40px; }

  .company-name {
    position: absolute; left: 54px; top: 46px;
    font-size: 28px; font-weight: 400; line-height: 36px; color: var(--ink);
  }
  .person {
    position: absolute; left: 52px; top: 264px;
  }
  .person__name {
    font-size: 36px; font-weight: 700; color: var(--purple); line-height: 36px;
  }
  .person__credentials { font-size: 14px; font-weight: 600; color: var(--ink); margin-left: 3px; }
  .person__title { font-size: 16px; font-weight: 600; color: var(--ink); line-height: 20px; margin-top: 4px; }
  .contact { list-style: none; font-size: 17px; color: var(--blue); line-height: 21.5px; }

  .services {
    position: absolute; right: 60px; top: 308px;
    text-align: right; font-size: 17px; font-weight: 300; line-height: 30px;
    color: var(--line-blue);
  }
</style>
</head>
<body>
  <section class="card card--back" aria-label="Card back">
    <p class="back-statement">
      We are certified by the Ongoing Professional Lawyer Studies (OPLS) Council<br>
      of the Prairie High Tribunal to provide<br>
      Continuing Legal Education (CLE)&nbsp; credits to Illinois attorneys.
    </p>
    <p class="back-call">Call about what courses we offer! (555) 214-3092</p>
    <div class="brand-mark"><span class="brand-mark__dot"></span><span>HWAE</span></div>
  </section>

  <section class="card card--front" aria-label="Card front">
    <h1 class="company-name">Harborview Wellness Advising<br>&amp; Education LLC</h1>
    <div class="brand-mark"><span class="brand-mark__dot"></span><span>HWAE</span></div>
    <div class="person">
      <p class="person__name">Delia Marsh<span class="person__credentials">M.S.W., LCSW</span></p>
      <p class="person__title">Clinical Therapist &amp; Trainer</p>
      <ul class="contact">
        <li>counselordelia@mailbrook.net</li>
        <li>www.harborviewwellnessadvising.com</li>
        <li>(555) 214-3092</li>
        <li>Cedarvale, IL 60999</li>
      </ul>
    </div>
    <p class="services">
      Providing clinical therapy services to<br>
      individuals, families, couples, and children.<br>
      We also provide life coaching and crisis training.
    </p>
  </section>
</body>
</html>
```